Company letter head and business card for new Indian Pharmaceutical Export company.

We need a letterhead and business card design for an Indian Pharmaceutical Export company.

The letter head needs to contain the following information.
Vorin Healthline Pvt. Ltd.
Office No 4827 Plot No 19, Larkspire, KT Lane, 400153, Maharashtra, India.
Email: info@vorin-healthline.com
Phone: +91-8342196507
CIN: U71853MH2025PTC902617
GSTIN: (This number is still pending, we will add later)

The business card needs to contain:
Address:
Vorin Healthline Pvt. Ltd.
Office No 4827 Plot No19, Larkspire, KT Lane, 400153, MH, India.
Email: torvald@vorin-healthline.com
Phone: +49-17634902851
Name on card: Torvald Ramming
Position: Director

The design for the letter head and business card should be simple but trustworthy.
Please use only Green and blue, same as in the attached logo.

```html
<!DOCTYPE html>
<html lang="en">
<head>
<meta charset="utf-8">
<title>Vorin Healthline – Business Card</title>
<link rel="stylesheet" href="https://fonts.googleapis.com/css2?family=Montserrat:wght@400;500;600;800&display=swap">
<style>
  :root {
    --brand-blue: #1d6fb8;
    --brand-blue-deep: #0d5ea6;
    --brand-green: #6cc92e;
    --ink: #1c1c1c;
    --card: #ffffff;
    --backdrop: #e6e9ec;
  }
  * { box-sizing: border-box; margin: 0; padding: 0; }
  html, body {
    width: 1200px; height: 1200px; overflow: hidden;
    background: var(--backdrop);
    font-family: "Montserrat", Arial, sans-serif;
  }
  .sheet {
    width: 1200px; height: 1200px;
    display: flex; flex-direction: column; align-items: center; justify-content: center;
    gap: 60px;
  }
  .card {
    position: relative;
    width: 880px; height: 503px;
    background: var(--card);
    border-radius: 34px;
    overflow: hidden;
    box-shadow: 0 10px 28px rgba(0,0,0,.14);
  }

  /* front */
  .card-front .contact {
    position: absolute; left: 74px; top: 170px;
    color: var(--ink);
  }
  .holder-name {
    color: var(--brand-green);
    font-weight: 500; font-size: 34px; letter-spacing: 1px;
    text-transform: uppercase; line-height: 1.05;
  }
  .holder-role { font-size: 26px; font-weight: 400; margin-bottom: 26px; }
  .contact-list { list-style: none; font-size: 17px; line-height: 1.3; }
  .contact-list li { display: flex; gap: 12px; align-items: flex-start; margin-bottom: 4px; }
  .contact-list svg { flex: none; width: 20px; height: 20px; margin-top: 1px; fill: var(--brand-green); }
  .brand-front {
    position: absolute; right: 70px; top: 70px;
    width: 300px; display: flex; flex-direction: column; align-items: center; gap: 22px;
  }
  .brand-dot { width: 150px; height: 150px; border-radius: 50%; background: var(--brand-blue); }
  .brand-name {
    color: var(--brand-blue-deep);
    font-weight: 800; font-size: 32px; white-space: nowrap;
  }
  .band-green, .band-blue { position: absolute; bottom: 0; }
  .band-green { left: 0; width: 64%; height: 20px; background: var(--brand-green); }
  .band-blue { left: 65.5%; right: 0; height: 40px; background: var(--brand-blue); }

  /* back */
  .card-back { display: flex; flex-direction: column; align-items: center; justify-content: center; gap: 30px; }
  .card-back .brand-dot { width: 200px; height: 200px; }
  .card-back .brand-name { font-size: 44px; }
</style>
</head>
<body>
<main class="sheet">
  <section class="card card-front" aria-label="Business card front">
    <div class="contact">
      <h1 class="holder-name">Torvald Ramming</h1>
      <p class="holder-role">Director</p>
      <ul class="contact-list">
        <li><svg viewBox="0 0 24 24" aria-hidden="true"><path d="M6.6 10.8a15.1 15.1 0 0 0 6.6 6.6l2.2-2.2a1 1 0 0 1 1-.25 11.4 11.4 0 0 0 3.6.57 1 1 0 0 1 1 1V20a1 1 0 0 1-1 1A17 17 0 0 1 3 4a1 1 0 0 1 1-1h3.5a1 1 0 0 1 1 1c0 1.25.2 2.45.57 3.57a1 1 0 0 1-.25 1z"/></svg><span>+49-17634902851</span></li>
        <li><svg viewBox="0 0 24 24" aria-hidden="true"><path d="M2 5h20v14H2zm2 2v.5l8 5 8-5V7zm0 3v7h16v-7l-8 5z"/></svg><span>torvald@vorin-healthline.com</span></li>
        <li><svg viewBox="0 0 24 24" aria-hidden="true"><path d="M12 2a7 7 0 0 0-7 7c0 5.25 7 13 7 13s7-7.75 7-13a7 7 0 0 0-7-7zm0 9.5A2.5 2.5 0 1 1 12 6.5a2.5 2.5 0 0 1 0 5z"/></svg><span>Vorin Healthline Pvt. Ltd.<br>Office No 4827 Plot No19,<br>Larkspire, KT Lane, 400153, MH, India.</span></li>
      </ul>
    </div>
    <div class="brand-front">
      <span class="brand-dot" aria-hidden="true"></span>
      <span class="brand-name">Vorin Healthline</span>
    </div>
    <span class="band-green" aria-hidden="true"></span>
    <span class="band-blue" aria-hidden="true"></span>
  </section>

  <section class="card card-back" aria-label="Business card back">
    <span class="brand-dot" aria-hidden="true"></span>
    <span class="brand-name">Vorin Healthline</span>
  </section>
</main>
</body>
</html>
```